accomplished personal trainer, former elite gymnast from Russia, highly professional and experienced

Established Fitness trainer in California requires a new web site to attract personal clients and build her group exercise classes.

Here is an example of another fitness trainer's site that I really liked the technology:
http://www.tedmolvin.com

Below I have inserted my current web site: www.quorbalfitnesslodi.com
You can use this web site for the principal content, such as my background and qualifications.

Target Market(s)

Anyone who wants to improve their fitness levels and wellness in general. Anyone who needs directions and instruction on how to exercise. I can train anyone from elite athlete to a disabled person.

Industry/Entity Type

Fitness

Coding

Coded - Design and coding required

Number of Pages Required

5+ page

Font styles to use
Sans Serif

Requirements
Must have
• Easy to navigate main info about me, location, services, contact, benefits of using my services.
• Would be great to create unique representation of me as a trainer and a person, using new technologies and new ideas. Make it different from the other websites. Having its own character. Not too complicated and heavy with information, but an eye catching, useful and fun to navigate.
Nice to have
• new technology, easy access to information, the idea of enjoyment of life, lightness about achieving any goal, spiritual wisdom, unique design. I am planning to insert educational videos, advise, maybe jokes. Sign in, shopping cart, logo, should be easy for me to make changes in content.
Should not have
• cliché, outdated technology, too complicated,

```html
<!DOCTYPE html>
<html lang="en">
<head>
<meta charset="utf-8">
<title>Quorbal Fitness Lodi</title>
<link rel="stylesheet" href="https://fonts.googleapis.com/css2?family=Roboto+Condensed:wght@400;700&family=Open+Sans:wght@400;600;700&display=swap">
<style>
:root{
  --green:#4cb000;
  --green-dark:#3a8c00;
  --ink:#222;
  --text:#555;
  --muted:#888;
  --line:#e3e3e3;
  --white:#fff;
  --footer:#1b1d1f;
  --footer-text:#9a9a9a;
  --photo-park:linear-gradient(135deg,#5f8a3a,#9ec16a 45%,#3f6b2a);
  --photo-dark:linear-gradient(135deg,#2a2a2a,#4a3f38);
}
*{margin:0;padding:0;box-sizing:border-box}
html,body{width:1200px;height:4500px;overflow:hidden;background:var(--white)}
body{position:relative;font-family:"Open Sans",sans-serif;color:var(--text)}
.abs{position:absolute}
.photo{position:absolute;left:0;width:1200px}
h2.section-title{position:absolute;left:0;width:1200px;text-align:center;font-family:"Roboto Condensed",sans-serif;font-weight:700;font-size:36px;color:var(--ink);letter-spacing:1px}
h2.section-title span{color:var(--green)}
.title-rule{position:absolute;left:540px;width:120px;height:3px;background:var(--green)}

/* top bar */
.topbar{top:0;left:0;width:1200px;height:45px;background:var(--white)}
.topbar-call{left:0;top:0;width:330px;height:45px;background:var(--green);color:var(--white);font-size:13px;font-weight:600;line-height:45px;padding-left:60px}
.topbar-call svg{position:absolute;left:30px;top:14px}
.socials{right:30px;top:9px;display:flex;gap:10px}
.socials i{display:block;width:27px;height:27px;border-radius:50%;background:#333}

/* hero */
.hero{top:45px;height:600px;background:var(--photo-park)}
.header{left:30px;top:60px;width:1140px;height:90px;background:var(--white);box-shadow:0 2px 6px rgba(0,0,0,.15)}
.brand{left:30px;top:25px;font-family:"Roboto Condensed",sans-serif;font-weight:700;font-size:34px;color:var(--ink);letter-spacing:1px}
.nav{right:20px;top:34px;display:flex;gap:66px;font-size:14px;color:#333;font-weight:600}
.hero-title{left:390px;top:335px;width:420px;height:75px;background:rgba(0,0,0,.45);color:var(--white);text-align:center;font-family:"Roboto Condensed",sans-serif;font-size:46px;line-height:75px;letter-spacing:1px}
.hero-btn{left:525px;top:410px;width:150px;height:42px;border:2px solid var(--white);color:var(--white);text-align:center;font-size:14px;line-height:38px;font-weight:600;background:rgba(0,0,0,.25)}

/* about */
.about-photo{left:45px;top:700px;width:250px;height:325px;background:var(--photo-dark)}
.about-text{left:500px;top:690px;width:640px}
.about-text h2{font-family:"Roboto Condensed",sans-serif;font-weight:700;font-size:36px;color:var(--ink)}
.about-text h2 span{color:var(--green)}
.about-text .rule{width:140px;height:3px;background:var(--green);margin:8px 0 22px}
.about-text p{font-size:15px;line-height:23px;margin-bottom:22px}
.about-text strong{font-size:15px;color:#333}
.about-text ul{list-style:none;margin-top:12px}
.about-text li{font-size:15px;line-height:24px;padding-left:18px;position:relative}
.about-text li:before{content:"";position:absolute;left:2px;top:10px;width:6px;height:6px;background:var(--green)}

/* trainers */
.trainer{top:1575px;width:343px}
.trainer-photo{width:343px;height:340px;background:linear-gradient(160deg,#c9b9a8,#e6ded4 50%,#8d8a86)}
.trainer-card{position:absolute;left:35px;top:285px;width:273px;height:55px;background:var(--white)}
.trainer-icons{position:absolute;left:0;top:300px;width:343px;display:flex;justify-content:center;gap:28px}
.trainer-icons i{display:block;width:34px;height:34px;transform:rotate(45deg);border:1px solid var(--line);background:#f4f4f4}
.trainer-role{position:absolute;top:370px;width:343px;text-align:center;font-size:12px;color:#e23a3a}
.trainer-name{position:absolute;top:395px;width:343px;text-align:center;font-family:"Roboto Condensed",sans-serif;font-size:16px;color:#333;letter-spacing:1px}

/* testimonial */
.avatar{left:530px;top:2570px;width:140px;height:140px;border-radius:50%;border:4px solid #eee;background:linear-gradient(135deg,#7fb3d9,#e8c5a8)}
.arrow{top:2640px;width:30px;height:30px;border:1px solid #bbb;border-radius:50%}
.quote{left:180px;top:2750px;width:840px;text-align:center;font-size:15px;line-height:25px;color:#666}
.quote-name{left:0;top:2855px;width:1200px;text-align:center;color:var(--green);font-size:17px;font-weight:600}

/* nutrition */
.nutri-photo{left:50px;top:3470px;width:400px;height:215px;background:radial-gradient(ellipse at 50% 45%,#e04a2c,#f3c56a 40%,#f4f4f4 70%)}
.nutri-text{left:500px;top:3455px;width:640px;font-size:15px;line-height:27px;color:#444}
.nutri-btn{left:500px;top:3635px;width:170px;height:48px;border:2px solid #333;text-align:center;line-height:44px;font-size:13px;font-weight:600;color:#333}

/* footer */
.footer{top:3745px;left:0;width:1200px;height:755px;background:var(--footer)}
.contact-box{top:3815px;width:330px;height:120px;border:1px solid #3b3d3f}
.contact-box .icon{position:absolute;left:25px;top:-20px;width:45px;height:45px;background:var(--green)}
.contact-box .icon svg{position:absolute;left:12px;top:12px}
.contact-box h4{position:absolute;left:25px;top:40px;font-size:15px;color:var(--white);font-weight:600}
.contact-box p{position:absolute;left:25px;top:66px;font-size:13px;line-height:20px;color:var(--footer-text)}
.foot-brand{left:45px;top:4055px;font-family:"Roboto Condensed",sans-serif;font-weight:700;font-size:22px;color:var(--white);letter-spacing:1px}
.foot-about{left:45px;top:4095px;width:220px;font-size:12px;line-height:18px;color:var(--footer-text)}
.foot-social{left:45px;top:4280px;display:flex;gap:12px}
.foot-social i{display:block;width:30px;height:30px;background:#3a3c3e}
.foot-col{top:4040px;font-size:13px;color:var(--footer-text)}
.foot-col h5{font-size:14px;color:var(--white);font-weight:600;margin-bottom:18px}
.foot-col li{list-style:none;line-height:37px;border-bottom:1px solid #2c2e30;width:180px}
.hours dt{color:var(--white);font-size:13px;margin-top:14px}
.hours dd{font-size:13px;color:var(--footer-text);line-height:20px}
.copyright{left:0;top:4428px;width:1200px;text-align:center;font-size:13px;color:#ccc}
</style>
</head>
<body>

<div class="abs topbar">
  <div class="abs topbar-call">
    <svg width="16" height="16" viewBox="0 0 24 24"><path fill="#fff" d="M6.6 10.8a15 15 0 0 0 6.6 6.6l2.2-2.2a1 1 0 0 1 1-.25 11 11 0 0 0 3.6.6 1 1 0 0 1 1 1V20a1 1 0 0 1-1 1A17 17 0 0 1 3 4a1 1 0 0 1 1-1h3.5a1 1 0 0 1 1 1 11 11 0 0 0 .6 3.6 1 1 0 0 1-.25 1z"/></svg>
    Any Questions? Call Us (555) 014-2281
  </div>
  <div class="abs socials"><i></i><i></i><i></i><i></i></div>
</div>

<div class="photo hero" role="img" aria-label="Group of people doing squats outdoors on a sunny park lawn"></div>
<header class="abs header">
  <div class="abs brand">QUORBAL FITNESS LODI</div>
  <nav class="abs nav"><span>HOME</span><span>ABOUT ME</span><span>LOCATION</span><span>SERVICES</span><span>CONTACT</span></nav>
</header>
<div class="abs hero-title">FITNESS OUTDOORS</div>
<div class="abs hero-btn">CONTACT US</div>

<section>
  <div class="abs about-photo" role="img" aria-label="Portrait of the trainer in athletic wear against a dark background"></div>
  <div class="abs about-text">
    <h2>EXERCISE <span>TRAINING</span></h2>
    <div class="rule"></div>
    <p>Vera Solnova is the owner of Quorbal Fitness. She was born and raised in Vologda, Russia where she was a competitive gymnast. Vera graduated from Northern Academy of Sport with a bachelor degree in Kinesiology and Sports Science.</p>
    <p>For more than 20 years, Vera has worked as choreographer, gymnastics coach, and fitness professional.</p>
    <strong>Certified by NFCB as a :</strong>
    <ul>
      <li>Personal Trainer</li>
      <li>Group Exercise Instructor</li>
      <li>Medical Exercise Specialist</li>
      <li>Orthopedic Exercise Specialist</li>
    </ul>
  </div>
</section>

<div class="photo" style="top:1055px;height:395px;background:var(--photo-park)" role="img" aria-label="Woman in pink top stretching outdoors in a green park"></div>

<section>
  <h2 class="section-title" style="top:1480px">WORLD BEST <span>TRAINERS</span></h2>
  <div class="title-rule" style="top:1535px"></div>
  <div class="abs trainer" style="left:57px">
    <div class="trainer-photo" role="img" aria-label="Personal trainer with a class in the gym"></div>
    <div class="trainer-card"></div>
    <div class="trainer-icons"><i></i><i></i><i></i></div>
    <div class="trainer-role">Personal Trainer</div>
    <div class="trainer-name">MARLA QUINT</div>
  </div>
  <div class="abs trainer" style="left:428px">
    <div class="trainer-photo" role="img" aria-label="Pilates trainer with a towel over his shoulders"></div>
    <div class="trainer-card"></div>
    <div class="trainer-icons"><i></i><i></i><i></i></div>
    <div class="trainer-role">Pilates Trainer</div>
    <div class="trainer-name">DEVON RUSK</div>
  </div>
  <div class="abs trainer" style="left:799px">
    <div class="trainer-photo" role="img" aria-label="Weight trainer sitting beside gym equipment"></div>
    <div class="trainer-card"></div>
    <div class="trainer-icons"><i></i><i></i><i></i></div>
    <div class="trainer-role">Weight Trainer</div>
    <div class="trainer-name">TESSA HARLOW</div>
  </div>
</section>

<div class="photo" style="top:2050px;height:390px;background:var(--photo-park)" role="img" aria-label="Group exercise class stretching arms overhead among trees"></div>

<section>
  <h2 class="section-title" style="top:2480px">WHAT OUR HAPPY <span>CLIENTS SAYS</span></h2>
  <div class="title-rule" style="top:2535px"></div>
  <div class="abs avatar" role="img" aria-label="Client photo in a circular frame"></div>
  <div class="abs arrow" style="left:195px"><svg width="28" height="28" viewBox="0 0 28 28"><path d="M16 9l-5 5 5 5" fill="none" stroke="#999" stroke-width="2"/></svg></div>
  <div class="abs arrow" style="left:975px"><svg width="28" height="28" viewBox="0 0 28 28"><path d="M12 9l5 5-5 5" fill="none" stroke="#999" stroke-width="2"/></svg></div>
  <p class="abs quote">Nullam porttitor lacus a lorem consectetur aliquet. Aenean rutrum augue mauris. Cras elit nibh, malesuada eget sodales non, dignissim eget elit. Quisque lectus mi, posuere non elit nec, imperdiet pulvinar leo. Curabitur semper id massa id pulvinar.</p>
  <div class="abs quote-name">Nadia Crest</div>
</section>

<div class="photo" style="top:2930px;height:390px;background:var(--photo-park)" role="img" aria-label="Women training with suspension straps outdoors"></div>

<section>
  <h2 class="section-title" style="top:3370px">NUTRITION <span>COACHING</span></h2>
  <div class="title-rule" style="top:3425px"></div>
  <div class="abs nutri-photo" role="img" aria-label="Plate of fresh vegetables with a measuring tape"></div>
  <p class="abs nutri-text">Lorem Ipsum is simply dummy text of the printing and typesetting industry. Lorem Ipsum has been the industry's standard dummy text ever since the 1500s, when an unknown printer took a galley of type and scrambled it to make a type specimen book. It has survived not only five centuries, but also the leap into electronic typesetting, remaining essentially unchanged.</p>
  <div class="abs nutri-btn">LEARN MORE</div>
</section>

<footer>
  <div class="abs footer" role="img" aria-label="Dark gym background with kettlebells and an athlete training"></div>
  <div class="abs contact-box" style="left:45px">
    <div class="icon"><svg width="20" height="20" viewBox="0 0 24 24"><path fill="#fff" d="M12 2a7 7 0 0 0-7 7c0 5 7 13 7 13s7-8 7-13a7 7 0 0 0-7-7zm0 9.5A2.5 2.5 0 1 1 12 6.5a2.5 2.5 0 0 1 0 5z"/></svg></div>
    <h4>ADDRESS</h4>
    <p>09 Quorbal Fitness Lodi<br>Street 5, Victoria, England</p>
  </div>
  <div class="abs contact-box" style="left:435px">
    <div class="icon"><svg width="20" height="20" viewBox="0 0 24 24"><path fill="#fff" d="M3 5h18v14H3zM3 5l9 7 9-7" stroke="#4cb000" stroke-width="1.5"/></svg></div>
    <h4>MAIL US</h4>
    <p>Get Support Via<br>hello@quorballodi.net</p>
  </div>
  <div class="abs contact-box" style="left:825px">
    <div class="icon"><svg width="20" height="20" viewBox="0 0 24 24"><path fill="#fff" d="M6.6 10.8a15 15 0 0 0 6.6 6.6l2.2-2.2a1 1 0 0 1 1-.25 11 11 0 0 0 3.6.6 1 1 0 0 1 1 1V20a1 1 0 0 1-1 1A17 17 0 0 1 3 4a1 1 0 0 1 1-1h3.5a1 1 0 0 1 1 1 11 11 0 0 0 .6 3.6 1 1 0 0 1-.25 1z"/></svg></div>
    <h4>PHONE / FAX</h4>
    <p>+1 123 456 789<br>+1 123 456 789</p>
  </div>

  <div class="abs foot-brand">QUORBAL FITNESS LODI</div>
  <p class="abs foot-about">Our studio offers friendly personal training and group classes for every level. We help you build strength, balance and confidence with a plan made for your body, your goals and your daily life, indoors or outdoors.</p>
  <div class="abs foot-social"><i></i><i></i><i></i><i></i></div>

  <div class="abs foot-col" style="left:315px">
    <h5>Pages</h5>
    <ul><li>About Us</li><li>Volunteers</li><li>Causes</li><li>Events</li><li>Blog</li><li>Contact</li></ul>
  </div>
  <div class="abs foot-col" style="left:585px">
    <h5>Quick Links</h5>
    <ul><li>Privacy Policy</li><li>Donor Privacy Policy</li><li>Disclaimer</li><li>Terms of Use</li><li>Copyright Notice</li><li>Media Center</li></ul>
  </div>
  <div class="abs foot-col hours" style="left:855px">
    <h5>Opening Hours</h5>
    <dl>
      <dt>Monday To Friday</dt><dd>9:00 am to 9:00 pm</dd>
      <dt>Monday To Friday</dt><dd>9:00 am to 9:00 pm</dd>
      <dt>Monday To Friday</dt><dd>9:00 am to 9:00 pm</dd>
    </dl>
  </div>

  <div class="abs copyright">© copyright 2016, All Rights Reserved <span style="color:#fff">Privacy Policy | Terms and Conditions</span></div>
</footer>

</body>
</html>
```